Bramwell's Cleaners new delivery postcard

We need to advertise for our new pick up and delivery dry cleaning/laundry service.
Mens Business Shirts $2.00
Pants $4.50
Skirts $5.00
Dry Clean Shirt/Blouse $5.00
Dress $9.00
2 Piece Suits $9.00
Updates
We would like to use a 5x7 size postcard, printed on both sides. We would like to add a discount to the card for 25% off of their first order, with the flyer.
We are a famly run dry cleaners. My name is Rosalind Tusk and my cell # is 614-203-4478. We are trying to expand our business to include free pick and delivery.
If possible can you use the logo I sent some where on the postcard? The phone # for the store is 614-392-0654.
Reason: Still need to get partners approval.
Industry/Entity Type
Business

```html
<!DOCTYPE html>
<html lang="en">
<head>
<meta charset="utf-8">
<title>Bramwell's Cleaners – Delivery Postcard</title>
<link href="https://fonts.googleapis.com/css2?family=Sorts+Mill+Goudy&family=Fjalla+One&family=Open+Sans:wght@700&display=swap" rel="stylesheet">
<style>
  :root {
    --page-bg: #1c1c1e;
    --card-white: #ffffff;
    --sky-light: #e3f1fb;
    --sky-mid: #bfe0f5;
    --brand-blue: #1f4f9c;
    --brand-navy: #1b3c82;
    --icon-blue: #8fcdee;
    --label-blue: #6cb8e3;
    --text-grey: #4a4a4a;
    --sign-blue: #2a5fb5;
    --sign-dark: #173f86;
    --deal-red: #d91f26;
    --stamp-grey: #e4e6f2;
  }
  * { margin: 0; padding: 0; box-sizing: border-box; }
  html, body { width: 1200px; height: 1191px; overflow: hidden; background: var(--page-bg); }
  .canvas { position: relative; width: 1200px; height: 1191px; }

  .postcard {
    position: absolute; width: 737px; height: 571px; overflow: hidden;
    font-variant-numeric: lining-nums;
    background:
      radial-gradient(ellipse 60% 30% at 40% 62%, rgba(191,224,245,.75), transparent 70%),
      linear-gradient(165deg, var(--card-white) 0%, var(--sky-light) 45%, var(--card-white) 80%);
  }
  .postcard::after {
    content: ""; position: absolute; left: 0; right: 0; bottom: 0; height: 90px;
    background: repeating-linear-gradient(-55deg, rgba(200,215,230,.35) 0 1px, transparent 1px 9px);
  }
  .postcard--front { left: 44px; top: 46px; }
  .postcard--back { left: 413px; top: 566px; }

  .brand-name {
    position: absolute; font-family: "Sorts Mill Goudy", serif; font-size: 50px; font-weight: normal;
    color: var(--brand-blue); white-space: nowrap; line-height: 1;
  }
  .brand-tagline {
    position: absolute; font-family: "Sorts Mill Goudy", serif; font-size: 20px;
    color: var(--text-grey); white-space: nowrap;
  }

  .stamp-box { position: absolute; left: 566px; top: 30px; width: 138px; height: 142px; background: var(--stamp-grey); }

  .photo { position: absolute; z-index: 1; }
  .photo--clothes-stack {
    left: 0; top: 150px; width: 185px; height: 240px;
    background: linear-gradient(180deg, #ece9e4 0%, #4aa6d8 25%, #e8455b 50%, #f07fb0 72%, #f3a6c5 100%);
    border-radius: 0 14px 14px 0;
  }
  .photo--clothes-box {
    left: 432px; top: 372px; width: 270px; height: 172px;
    background: linear-gradient(170deg, #e36d8c 0%, #3aa45a 30%, #a05fa8 50%, #caa06c 70%, #b8874f 100%);
    border-radius: 6px;
  }

  .delivery-sign { position: absolute; width: 170px; height: 170px; z-index: 2; }
  .front-sign { left: 186px; top: 130px; }
  .back-sign { left: 492px; top: 50px; }

  .call-block { position: absolute; font-family: "Sorts Mill Goudy", serif; color: var(--brand-navy); text-align: right; z-index: 3; }
  .call-block--front { right: 400px; top: 385px; }
  .call-block--front .call-now { font-size: 26px; }
  .call-block--front .store-line { font-size: 25px; margin-top: 6px; white-space: nowrap; }

  .call-block--back {
    left: 385px; top: 268px; text-align: left; transform: rotate(-16deg); transform-origin: left top; white-space: nowrap;
  }
  .call-block--back .contact-name { font-size: 19px; }
  .call-block--back .call-now { font-size: 34px; line-height: .95; }
  .call-block--back .cell-line { font-size: 34px; line-height: .95; }

  .service-icons { position: absolute; left: 54px; top: 131px; display: flex; gap: 14px; }
  .service { width: 90px; text-align: center; }
  .service-circle { display: block; width: 90px; height: 90px; }
  .service-label {
    display: block; margin-top: 8px; font-family: "Open Sans", sans-serif; font-weight: 700;
    font-size: 9px; letter-spacing: 1px; color: var(--label-blue);
  }

  .price-list {
    position: absolute; left: 58px; top: 248px; list-style: none;
    font-family: "Sorts Mill Goudy", serif; font-size: 19px; color: var(--text-grey);
  }
  .price-list li { height: 29.4px; white-space: nowrap; }
  .price-list li::before { content: "●"; color: var(--brand-navy); font-size: 12px; margin-right: 5px; vertical-align: 2px; }
  .price-list b { font-weight: normal; color: #111; }

  .discount-tag { position: absolute; left: 20px; top: 430px; width: 230px; height: 115px; }
  .discount-note {
    position: absolute; left: 258px; top: 474px; font-family: "Sorts Mill Goudy", serif; color: var(--brand-navy);
  }
  .discount-note .small { font-size: 18px; display: block; }
  .discount-note .large { font-size: 28px; display: block; line-height: 1; }
  .pointer-arrow { position: absolute; left: 604px; top: 222px; width: 42px; height: 46px; }
</style>
</head>
<body>
<main class="canvas">

  <section class="postcard postcard--front" aria-label="Postcard address side">
    <h1 class="brand-name" style="left:52px; top:42px;">Bramwell's Cleaners</h1>
    <p class="brand-tagline" style="left:200px; top:96px;">dry cleaning / laundry service</p>
    <div class="stamp-box" aria-label="Postage stamp area"></div>
    <div class="photo photo--clothes-stack" role="img" aria-label="Photo of a stack of neatly folded colourful laundry with flowers"></div>

    <svg class="delivery-sign front-sign" viewBox="0 0 170 170" aria-label="Free pick up and delivery sign">
      <circle cx="73" cy="8" r="7" fill="#d8dde3"/>
      <path d="M73 10 L18 66 M73 10 L138 60" stroke="#777" stroke-width="1"/>
      <g transform="rotate(6 85 110)">
        <rect x="8" y="62" width="150" height="98" rx="16" fill="var(--sign-blue)"/>
        <text x="82" y="112" text-anchor="middle" font-family="Fjalla One, sans-serif" font-size="50" fill="#fff">free</text>
        <rect x="36" y="118" width="96" height="30" fill="var(--sign-dark)"/>
        <text x="84" y="131" text-anchor="middle" font-family="Fjalla One, sans-serif" font-size="12" fill="#fff">pick up and</text>
        <text x="84" y="145" text-anchor="middle" font-family="Fjalla One, sans-serif" font-size="12" fill="#fff">delivery</text>
        <circle cx="50" cy="152" r="4" fill="#fff"/><circle cx="118" cy="152" r="4" fill="#fff"/>
      </g>
    </svg>

    <div class="call-block call-block--front">
      <p class="call-now">Call Us Now</p>
      <p class="store-line">Store # is 614-392-0654</p>
    </div>
  </section>

  <section class="postcard postcard--back" aria-label="Postcard offer side">
    <h2 class="brand-name" style="left:58px; top:37px;">Bramwell's Cleaners</h2>
    <p class="brand-tagline" style="left:212px; top:92px;">dry cleaning / laundry service</p>

    <div class="service-icons">
      <div class="service">
        <svg class="service-circle" viewBox="0 0 90 90" aria-hidden="true">
          <circle cx="45" cy="45" r="45" fill="var(--icon-blue)"/>
          <rect x="28" y="22" width="34" height="46" rx="2" fill="#fff"/>
          <circle cx="45" cy="48" r="11" fill="none" stroke="var(--icon-blue)" stroke-width="3"/>
          <line x1="30" y1="30" x2="60" y2="30" stroke="var(--icon-blue)" stroke-width="1.5"/>
        </svg>
        <span class="service-label">WASH</span>
      </div>
      <div class="service">
        <svg class="service-circle" viewBox="0 0 90 90" aria-hidden="true">
          <circle cx="45" cy="45" r="45" fill="var(--icon-blue)"/>
          <path d="M18 56 Q24 36 48 34 L66 34 Q72 34 72 42 L72 56 Z" fill="#fff"/>
          <path d="M36 34 Q44 24 58 26" stroke="#fff" stroke-width="4" fill="none"/>
        </svg>
        <span class="service-label">PRESS</span>
      </div>
      <div class="service">
        <svg class="service-circle" viewBox="0 0 90 90" aria-hidden="true">
          <circle cx="45" cy="45" r="45" fill="var(--icon-blue)"/>
          <rect x="24" y="22" width="42" height="48" rx="2" fill="#fff"/>
          <circle cx="52" cy="42" r="9" fill="none" stroke="var(--icon-blue)" stroke-width="3"/>
          <rect x="28" y="26" width="10" height="6" fill="var(--icon-blue)"/>
          <line x1="24" y1="60" x2="66" y2="60" stroke="var(--icon-blue)" stroke-width="1.5"/>
        </svg>
        <span class="service-label">DRY CLEAN</span>
      </div>
    </div>

    <ul class="price-list">
      <li>Mens Business Shirts <b>$2.00</b></li>
      <li>Pants <b>$4.50</b></li>
      <li>Skirts <b>$5.00</b></li>
      <li>Dry Clean Shirt/Blouse <b>$5.00</b></li>
      <li>Dress <b>$9.00</b></li>
      <li>2 Piece Suits <b>$9.00</b></li>
    </ul>

    <svg class="discount-tag" viewBox="0 0 230 115" aria-label="25% off">
      <rect x="200" y="32" width="28" height="80" fill="#ddd" stroke="#999" stroke-dasharray="4 3"/>
      <path d="M50 40 L205 22 L222 88 L58 112 Z" fill="var(--deal-red)"/>
      <g transform="rotate(-8 65 78)">
        <rect x="38" y="52" width="52" height="52" transform="rotate(45 64 78)" fill="#fff"/>
        <rect x="43" y="57" width="42" height="42" transform="rotate(45 64 78)" fill="var(--deal-red)"/>
        <text x="64" y="87" text-anchor="middle" font-family="Fjalla One, sans-serif" font-size="26" fill="#fff">25<tspan font-size="13">%</tspan></text>
        <text x="148" y="93" text-anchor="middle" font-family="Fjalla One, sans-serif" font-size="42" fill="#fff">OFF</text>
      </g>
    </svg>
    <p class="discount-note"><span class="small">of their</span><span class="large">first order</span></p>

    <svg class="delivery-sign back-sign" viewBox="0 0 170 170" aria-label="Free pick up and delivery sign">
      <circle cx="80" cy="10" r="7" fill="#d8dde3"/>
      <path d="M80 12 L30 72 M80 12 L140 74" stroke="#777" stroke-width="1"/>
      <rect x="12" y="68" width="150" height="98" rx="16" fill="var(--sign-blue)"/>
      <text x="86" y="118" text-anchor="middle" font-family="Fjalla One, sans-serif" font-size="50" fill="#fff">free</text>
      <rect x="40" y="124" width="96" height="30" fill="var(--sign-dark)"/>
      <text x="88" y="137" text-anchor="middle" font-family="Fjalla One, sans-serif" font-size="12" fill="#fff">pick up and</text>
      <text x="88" y="151" text-anchor="middle" font-family="Fjalla One, sans-serif" font-size="12" fill="#fff">delivery</text>
      <circle cx="56" cy="158" r="4" fill="#fff"/><circle cx="122" cy="158" r="4" fill="#fff"/>
    </svg>

    <svg class="pointer-arrow" viewBox="0 0 42 46" aria-hidden="true">
      <path d="M36 2 L34 30 L8 36" stroke="var(--brand-navy)" stroke-width="4" fill="none"/>
      <path d="M2 37 L14 28 L14 44 Z" fill="var(--brand-navy)"/>
    </svg>

    <div class="call-block call-block--back">
      <p class="contact-name">Rosalind Tusk</p>
      <p class="call-now">Call Us Now</p>
      <p class="cell-line">614-203-4478</p>
    </div>

    <div class="photo photo--clothes-box" role="img" aria-label="Photo of an open cardboard box filled with colourful clothes"></div>
  </section>

</main>
</body>
</html>
```